QV - menu design

Hi,

We require elegant menu design for upscale restaurant. Please find attached the logo and the menu items for your reference.

for inspiration, this is a good website: -
http://www.platewhisper.example/bellfoldnotes/about.php

We are very much open for Menu Size suggestions.

unfortunately the place is going under renovation, we don't have updated images to it. the closest look and feel to our place is http://varnelo.example ..

we are also open for creative options on the shape, the styles, etc. as long as it represents the fine dine feel ...

Thanks ...

Dear All,

We wouldlike to extend our apology for not being able to provide feedbacks on everysingle design. We were extremely busy and we have multiple contests opensimultaneously which makes the process even harder.

However,we would like to thank you all for the efforts you have put into designingour menu. It is very much appreciated …

We wishyou all success in your design ventures and we are quite positive that we willbe working with many of you on many projects in the soon future. 

Thanks & Regards,

TLG Team...

 

 

 

Industry/Entity Type

Restaurant

Requirements
Must have
• Please ensure that there are 'some' images in the menu ... this is very important.
Should not have
• IMPORTANT: -

1. Please DO NOT insert any currency sign to the menu
2. Please keep the prices of the menu at the end of the menu items descriptions NOT beside the menu item names. The font of the price should be similar to the menu item description and please DO NOT bold the numbers. the prices should be subtle.

Thank you ...

```html
<!DOCTYPE html>
<html lang="en">
<head>
<meta charset="utf-8">
<title>QV – Menu</title>
<link href="https://fonts.googleapis.com/css2?family=Pinyon+Script&family=Roboto+Condensed:wght@300;400&display=swap" rel="stylesheet">
<style>
  :root{
    --page-bg:#ffffff;
    --cream-light:#fdf5df;
    --cream:#f6e6bb;
    --cream-deep:#efd69c;
    --red-bright:#c9303f;
    --red:#a31d2a;
    --red-deep:#6b0f15;
    --gold:#d9a54a;
    --gold-light:#f1cf84;
    --gold-dark:#9c6a1f;
    --splash:#d9b873;
    --ink:#2a2520;
    --ink-soft:#3b332b;
    --rule:#6a6258;
  }
  *{margin:0;padding:0;box-sizing:border-box}
  html,body{width:1200px;height:1000px;overflow:hidden;background:var(--page-bg)}
  body{position:relative;font-family:"Roboto Condensed",Arial,sans-serif;color:var(--ink-soft)}

  .sheet{position:absolute;background:radial-gradient(ellipse at 55% 60%,var(--cream-light) 0%,var(--cream) 55%,var(--cream-deep) 100%);box-shadow:2px 3px 6px rgba(0,0,0,.35);overflow:hidden}
  .band{position:absolute;top:0;bottom:0;
    background:
      linear-gradient(to bottom,rgba(255,80,90,.15),rgba(0,0,0,0) 40%,rgba(40,0,0,.45)),
      linear-gradient(to right,var(--red-deep) 0,var(--red-bright) 14%,var(--red) 26%,var(--gold) 27%,var(--gold-light) 29%,var(--gold-dark) 31%,var(--red-deep) 32%,var(--red-bright) 50%,var(--red) 70%,var(--gold-dark) 72%,var(--gold-light) 75%,var(--gold) 78%,var(--red-deep) 80%,var(--red) 90%,var(--gold-dark) 92%,var(--gold-light) 95%,var(--gold) 100%)}
  .band.mirror{transform:scaleX(-1)}
  .trim{position:absolute;top:0;bottom:0;width:10px;background:linear-gradient(to right,var(--gold-dark),var(--gold-light) 40%,var(--gold) 70%,var(--gold-dark))}
  .splash{position:absolute;border-radius:50%;background:radial-gradient(circle,rgba(217,184,115,.45) 0%,rgba(217,184,115,0) 70%)}

  /* cover */
  .cover{left:41px;top:30px;width:261px;height:597px}
  .cover .band{left:0;width:37px}
  .cover .trim{left:37px}
  .flourish{position:absolute;left:70px;top:88px;width:160px;height:26px;background:radial-gradient(ellipse at center,rgba(217,165,74,.55) 0%,rgba(217,165,74,0) 70%)}
  .badge{position:absolute;left:110px;top:60px;width:78px;height:78px;border-radius:50%;background:radial-gradient(circle at 45% 30%,#555,#0b0b0b 65%);border:4px solid var(--gold);box-shadow:0 0 0 2px var(--gold-dark);display:flex;align-items:center;justify-content:center}
  .badge span{font-family:"Pinyon Script",cursive;font-size:19px;color:#f4ead2;line-height:1}
  .emblem-base{position:absolute;left:108px;top:458px;width:84px;height:84px;border-radius:50%;background:radial-gradient(circle,rgba(217,165,74,.9) 0%,rgba(200,150,60,.6) 55%,rgba(217,165,74,0) 72%)}
  .emblem{position:absolute;left:125px;top:475px;width:50px;height:50px;transform:rotate(45deg);background:radial-gradient(circle at 40% 40%,#3a3a3a,#0d0d0d);border:3px solid var(--gold)}
  .brand{position:absolute;left:0;right:0;text-align:center;font-family:"Roboto Condensed",Arial,sans-serif;font-weight:300;color:#1b1b1b;letter-spacing:2px;line-height:1}
  .cover .brand{top:242px;font-size:112px;padding-left:30px}

  /* spread */
  .spread{left:327px;top:53px;width:641px;height:813px}
  .spread .band.left{left:0;width:63px}
  .spread .trim.left{left:63px}
  .spread .band.right{right:0;width:62px}
  .spread .trim.right{right:62px}
  .spine{position:absolute;left:283px;top:0;width:60px;height:100%;background:linear-gradient(to right,rgba(120,85,30,0) 0,rgba(120,85,30,.25) 45%,rgba(80,55,20,.35) 50%,rgba(120,85,30,.2) 56%,rgba(120,85,30,0) 100%)}

  .section{position:absolute}
  .section h2{font-family:"Pinyon Script",cursive;font-weight:400;font-size:22px;color:#1c1a17;margin-bottom:13px;line-height:1;text-shadow:.4px 0 0 #1c1a17}
  .item{display:flex;justify-content:space-between;align-items:flex-end;font-size:11px;line-height:16.2px;margin-bottom:11.3px}
  .item.tight{margin-top:-11.3px}
  .price{flex:none;text-align:right;font-weight:300}
  .breakfast{left:97px;top:56px;width:191px}
  .sandwiches{left:352px;top:56px;width:193px}
  .soup{left:352px;top:516px;width:193px}
  .soup h2{margin-bottom:9px}
  .divider{position:absolute;left:352px;top:489px;width:193px;height:1px;background:var(--rule)}

  /* back */
  .back{left:893px;top:363px;width:284px;height:597px}
  .back .band{left:0;width:37px}
  .back .trim{left:37px}
  .contact{position:absolute;left:47px;right:0;top:209px;text-align:center;font-size:8.8px;line-height:12.2px;color:#2f2a24}
  .contact h3{font-family:"Pinyon Script",cursive;font-weight:400;font-size:17px;line-height:17px;color:#1c1a17;margin-bottom:12px;text-shadow:.3px 0 0 #1c1a17}
  .contact p{margin-bottom:8px}
  .back .rule{position:absolute;left:74px;top:379px;width:181px;height:1px;background:var(--rule)}
  .back .brand{top:440px;font-size:84px;padding-left:48px}
</style>
</head>
<body>

<section class="sheet cover">
  <div class="band"></div>
  <div class="trim" role="img" aria-label="Gold ornamental border strip"></div>
  <div class="splash" style="left:60px;top:0;width:110px;height:60px" role="img" aria-label="Faint ink splatter texture"></div>
  <div class="flourish" role="img" aria-label="Gold scroll flourish behind the badge"></div>
  <div class="badge" role="img" aria-label="Black and gold menu badge"><span>Menu</span></div>
  <div class="brand">QV</div>
  <div class="splash" style="left:70px;top:440px;width:70px;height:60px" role="img" aria-label="Faint ink splatter texture"></div>
  <div class="emblem-base" role="img" aria-label="Gold scalloped emblem with cutlery"></div>
  <div class="emblem"></div>
</section>

<section class="sheet spread">
  <div class="band left"></div>
  <div class="trim left" role="img" aria-label="Gold ornamental border strip"></div>
  <div class="band right mirror"></div>
  <div class="trim right" role="img" aria-label="Gold ornamental border strip"></div>
  <div class="spine"></div>
  <div class="splash" style="left:200px;top:10px;width:150px;height:90px" role="img" aria-label="Faint ink splatter texture"></div>
  <div class="splash" style="left:420px;top:0;width:150px;height:90px" role="img" aria-label="Faint ink splatter texture"></div>
  <div class="splash" style="left:80px;top:700px;width:140px;height:110px" role="img" aria-label="Faint ink splatter texture"></div>

  <div class="section breakfast">
    <h2>The Breakfast</h2>
    <div class="item"><span>Butter Croissant<br>Served plain with a selection of<br>two jams, a vanilla custard cream,<br>a chocolate Cream and butter curls)</span><span class="price">36</span></div>
    <div class="item"><span>Cheese Croissant<br>Crumbly freshly baked with<br>cheese filling</span><span class="price">29</span></div>
    <div class="item"><span>Daily Fresh Eggs<br>A choice of poached, scrambled,<br>pan fried, omelet) all served with<br>toasted Bread, mushrooms, roasted<br>tomatoes and chicken sausages</span><span class="price">59</span></div>
    <div class="item"><span>Healthy Time<br>One choice of hot beverage from<br>our cafe served with fruit salad,<br>natural Yoghurt, whole wheat bread<br>vegetable sandwiches and<br>sugar free biscuits selection</span><span class="price">49</span></div>
    <div class="item"><span>Energy Time<br>One choice of hot beverage from<br>our cafe served with finger chocolate<br>muffins, Poached egg with toasted bread<br>and crispy beef bacon, crepe roll with<br>goat Cheese and honey and finger<br>chocolate cream with salted cookies</span><span class="price">59</span></div>
    <div class="item"><span>QV Time<br>One choice of hot beverage from<br>our cafe served with our selection<br>of scones, Smoked salmon and<br>avocado sandwich, roasted sausages<br>sandwich, grilled vegetables sandwich,<br>selection of our best biscuits</span><span class="price">59</span></div>
    <div class="item"><span>The Arabic Breakfast<br>Choice of Zattar Manakish and<br>Cheese Manakish, served with<br>one choice of hot beverage from<br>our cafe and fresh orange juic</span><span class="price">59</span></div>
  </div>

  <div class="section sandwiches">
    <h2>The Sandwiches</h2>
    <div class="item"><span>Grilled Vegetables Sandwich<br>with fresh Goat cheese and<br>chives served with our<br>Homemade spicy garlic mayo</span><span class="price">59</span></div>
    <div class="item"><span>Butterfish burger with<br>fresh tomato, beef bacon, grilled<br>vegetables and béarnaise sauce</span><span class="price">XX</span></div>
    <div class="item"><span>Tataki Tuna sandwich with<br>red onion slices, stewed endives<br>and black olives and sultanas pate</span><span class="price">79</span></div>
    <div class="item"><span>Beef sirloin steak sandwich<br>with grain mustard, Parmesan<br>cheese and fresh Nashi pears</span><span class="price">79</span></div>
    <div class="item"><span>The Traditional Club sandwich<br>served with French fries and<br>vegetable chips</span><span class="price">69</span></div>
    <div class="item"><span>Chicken sandwich with Parmesan<br>cheese slices, sundried tomatoes<br>and mint flavored mayo</span><span class="price">69</span></div>
  </div>

  <div class="divider"></div>

  <div class="section soup">
    <h2>Soup</h2>
    <div class="item"><span>Bouillabaisse<br>Traditional French Seafood soup,<br>with Saffron and Estragon</span><span class="price">119</span></div>
    <div class="item tight"><span>Barley soup<br>With fresh vegetables, tomato<br>smoothie and a hint of garlic oil</span><span class="price">49</span></div>
    <div class="item"><span>Beef chili<br>Served with Arabic bread,<br>fresh guacamole and<br>spicy black beans</span><span class="price">49</span></div>
  </div>
</section>

<section class="sheet back">
  <div class="band"></div>
  <div class="trim" role="img" aria-label="Gold ornamental border strip"></div>
  <div class="splash" style="left:170px;top:20px;width:120px;height:90px" role="img" aria-label="Faint ink splatter texture"></div>
  <div class="contact">
    <h3>Contact</h3>
    <p>123 Address Place,<br>City Here, Country</p>
    <p>000 0000 0000<br>000 0000 0000</p>
    <p>email@websiteaddress.com<br>www.websiteaddress.com</p>
  </div>
  <div class="rule"></div>
  <div class="splash" style="left:60px;top:440px;width:80px;height:70px" role="img" aria-label="Faint ink splatter texture"></div>
  <div class="brand">QV</div>
</section>

</body>
</html>
```